Brennor Electronics, Inc. Business card

Incorporate a globe.
We repair electronics, sell electronic parts, and we recycle electronics. We've been in business since 1982. A technology feel to the card is preferred. I want to be able to give this card to a client from different industries and make it relate-able. I don't have a logo that I've been partial to in the past. It is not necessary in this case.

Target Market(s)

Consumer, Industrial, Business, Medical

Industry/Entity Type

Business

Contact Information for Business Card

5184 Mulvane Blvd. Dallas, TX 75319
214-508-3764 main 214-508-3719 fax
Gavin Tresaldo VP

Font styles to use
Serif

Requirements
Must have
• Technology feel
Nice to have
• Metallic look
Should not have
• no pastel colors

```html
<!DOCTYPE html>
<html lang="en">
<head>
<meta charset="utf-8">
<title>Brennor Electronics, Inc. – Business Card</title>
<link href="https://fonts.googleapis.com/css2?family=PT+Sans:wght@400;700&display=swap" rel="stylesheet">
<style>
  :root {
    --stage: #3b3430;
    --card: #141414;
    --card-edge: #1d1d1d;
    --foil: #8e8e8e;
    --text: #e4e4e4;
    --accent-red: #d8242c;
    --accent-orange: #e4572a;
  }
  * { box-sizing: border-box; margin: 0; padding: 0; }
  html, body {
    width: 1200px; height: 703px; overflow: hidden;
    background: var(--stage);
    font-family: "PT Sans", sans-serif;
  }
  .canvas {
    position: relative; width: 1200px; height: 703px;
    display: flex; align-items: center; justify-content: center; gap: 40px;
  }
  .card {
    position: relative; width: 520px; height: 297px;
    background: var(--card);
    border: 1px solid var(--card-edge);
    box-shadow: 0 10px 30px rgba(0,0,0,.45);
  }
  /* Front */
  .card--front .brand {
    position: absolute; left: 0; right: 0; top: 92px;
    display: flex; flex-direction: column; align-items: center; gap: 16px;
  }
  .brand__dot {
    width: 18px; height: 18px; border-radius: 50%;
    background: var(--foil);
  }
  .brand__name {
    font-size: 30px; font-weight: 400; color: var(--foil); letter-spacing: .2px;
    white-space: nowrap;
  }
  /* Back */
  .contact {
    position: absolute; left: 40px; top: 62px;
    color: var(--text); font-size: 14px; line-height: 19px;
  }
  .contact__name { color: var(--accent-red); font-weight: 700; font-size: 15px; }
  .contact__title { margin-bottom: 10px; }
  .contact__address { margin-bottom: 8px; }
  .contact__line { display: flex; align-items: center; gap: 8px; }
  .contact__icon {
    width: 12px; height: 12px; display: inline-flex; align-items: center; justify-content: center;
    color: var(--accent-red); font-size: 12px; font-weight: 700;
  }
  .card--back .brand {
    position: absolute; right: 34px; bottom: 60px;
    display: flex; flex-direction: column; align-items: flex-end; gap: 14px;
  }
  .card--back .brand__dot { background: var(--accent-red); margin-right: 80px; }
  .card--back .brand__name { color: var(--accent-orange); font-size: 24px; }
</style>
</head>
<body>
  <main class="canvas">
    <section class="card card--front" aria-label="Card front">
      <div class="brand">
        <span class="brand__dot"></span>
        <span class="brand__name">Brennor Electronics, Inc.</span>
      </div>
    </section>

    <section class="card card--back" aria-label="Card back">
      <div class="contact">
        <p class="contact__name">Gavin Tresaldo</p>
        <p class="contact__title">VP</p>
        <p class="contact__address">5184 Mulvane Blvd.<br>Dallas, TX 75319</p>
        <p class="contact__line">
          <span class="contact__icon">
            <svg width="11" height="11" viewBox="0 0 24 24" fill="currentColor"><path d="M6.6 10.8a15.1 15.1 0 0 0 6.6 6.6l2.2-2.2a1 1 0 0 1 1-.25 11.4 11.4 0 0 0 3.6.57 1 1 0 0 1 1 1V20a1 1 0 0 1-1 1A17 17 0 0 1 3 4a1 1 0 0 1 1-1h3.5a1 1 0 0 1 1 1c0 1.25.2 2.45.57 3.57a1 1 0 0 1-.25 1z"/></svg>
          </span>214-508-3764
        </p>
        <p class="contact__line">
          <span class="contact__icon">
            <svg width="8" height="12" viewBox="0 0 8 12" fill="none" stroke="currentColor" stroke-width="1.4"><rect x="1" y="1" width="6" height="10" rx="1"/></svg>
          </span>214-508-3719
        </p>
        <p class="contact__line"><span class="contact__icon">@</span>www.brennorcard.com</p>
        <p class="contact__line"><span class="contact__icon">@</span>info@brennorcard.com</p>
      </div>
      <div class="brand">
        <span class="brand__dot"></span>
        <span class="brand__name">Brennor Electronics, Inc.</span>
      </div>
    </section>
  </main>
</body>
</html>
```